Quorvantelle we are a young innovative brand about making life easier for people with a disability

Our tag line is Making Life Easy, we are still a relatively new company trying to bring innovation and excitement into the disability space - with latest products and technology - we do have existing website but need to unpgrade for a stronger visual presence.

```html
<!DOCTYPE html>
<html lang="en">
<head>
<meta charset="utf-8">
<title>Quorvantelle – Making Life Easy</title>
<link href="https://fonts.googleapis.com/css2?family=Montserrat:wght@600;700;800&family=Arimo:ital,wght@0,400;0,700;1,400&family=Saira:ital,wght@0,400;1,700&display=swap" rel="stylesheet">
<style>
:root{
  --red:#e01b1b;
  --red-dark:#a80f0f;
  --black:#111111;
  --ink:#222222;
  --text:#4a4a4a;
  --muted:#8a8a8a;
  --grey-bg:#f1f1f1;
  --white:#ffffff;
  --line:#d8d8d8;
}
*{box-sizing:border-box;margin:0;padding:0}
html,body{width:1200px;height:5133px;overflow:hidden}
body{font-family:"Arimo",Arial,sans-serif;color:var(--ink);background:var(--white);position:relative}
.heading{font-family:"Montserrat",sans-serif;font-weight:700;font-size:30px;text-align:center;color:var(--ink);letter-spacing:.3px}
.heading span{color:var(--red)}
.pill{display:inline-flex;align-items:center;justify-content:center;border:1.5px solid #9a9a9a;border-radius:20px;width:110px;height:32px;font-family:"Montserrat",sans-serif;font-size:10px;font-weight:700;color:var(--ink);background:var(--white)}
.arrow{position:absolute;width:20px;height:20px}
.arrow svg{display:block}

/* top bar */
.topbar{position:absolute;top:0;left:0;width:1200px;height:36px;background:var(--red);color:var(--white);font-family:"Montserrat",sans-serif;font-size:12px;font-weight:700}
.topbar .welcome{position:absolute;left:48px;top:10px}
.topbar .links{position:absolute;right:48px;top:10px;display:flex;gap:32px}

/* header */
.header{position:absolute;top:36px;left:0;width:1200px;height:96px;background:var(--white);border-bottom:1px solid #e6e6e6}
.brand{position:absolute;left:48px;top:28px;display:flex;align-items:center;gap:10px}
.brand-dot{width:40px;height:40px;border-radius:50%;background:var(--red)}
.brand-name{font-family:"Montserrat",sans-serif;font-weight:800;font-size:24px;color:var(--red)}
.nav{position:absolute;left:350px;top:38px;display:flex;gap:32px;font-family:"Arimo",sans-serif;font-weight:700;font-size:15px;color:var(--ink)}
.nav-icons{position:absolute;right:46px;top:35px;display:flex;gap:10px}
.nav-icons span{width:28px;height:28px;border-radius:50%;display:flex;align-items:center;justify-content:center}

/* hero */
.hero{position:absolute;top:132px;left:0;width:1200px;height:574px;overflow:hidden}
.hero-photo{position:absolute;inset:0;background:linear-gradient(180deg,#9aa1a7 0%,#6a6f74 45%,#2b2c2e 100%)}
.hero-panel{position:absolute;inset:0}
.hero-title{position:absolute;left:758px;top:178px;font-family:"Montserrat",sans-serif;font-weight:800;font-size:56px;line-height:56px;color:var(--white)}
.hero-btn{position:absolute;left:760px;top:320px;width:150px;height:48px;border-radius:24px;background:var(--black);color:var(--white);font-family:"Montserrat",sans-serif;font-weight:700;font-size:15px;display:flex;align-items:center;justify-content:center}
.hero-dots{position:absolute;left:822px;top:500px;display:flex;gap:14px}
.hero-dots i{display:block;width:34px;height:5px;background:rgba(255,255,255,.75)}

/* product rows */
.band{position:absolute;left:0;width:1200px}
.band.grey{background:var(--grey-bg)}
.cards{position:absolute;left:128px;display:flex;gap:24px}
.card{width:218px;height:312px;background:var(--white);border-radius:6px;display:flex;flex-direction:column;align-items:center;padding-top:20px}
.card .photo{width:150px;height:130px;border-radius:6px}
.card .name{margin-top:16px;font-size:14px;line-height:18px;color:var(--text);text-align:center;height:38px;width:180px}
.card .price{margin-top:6px;font-family:"Montserrat",sans-serif;font-weight:700;font-size:20px;color:var(--red)}
.card .pill{margin-top:12px}

/* categories */
.view-all{position:absolute;left:1015px;top:1350px;font-size:12px;font-weight:700;color:var(--red);text-decoration:underline}
.cat{position:absolute;border:3px solid var(--red);border-radius:4px;overflow:hidden;display:flex;align-items:flex-end;justify-content:center}
.cat .photo{position:absolute;inset:0}
.cat .label{position:relative;font-family:"Montserrat",sans-serif;font-weight:800;color:var(--white);margin-bottom:26px;font-size:16px}
.cat.big .label{font-size:21px;margin-bottom:46px}

/* customers */
.customer{position:absolute;top:2666px;height:490px}
.customer .quote{position:absolute;left:0;right:0;bottom:52px;text-align:center;color:var(--white)}
.customer .quote h3{font-family:"Montserrat",sans-serif;font-weight:700;font-size:18px;letter-spacing:.5px}
.customer .quote p{margin:14px auto 0;width:500px;font-style:italic;font-size:13px;line-height:17px}

/* video */
.video{position:absolute;top:3310px;left:0;width:1200px;height:600px;background:radial-gradient(ellipse at 60% 45%,#3a3d44 0%,#1c1e22 55%,#0c0c0e 100%)}
.play{position:absolute;left:562px;top:262px;width:76px;height:76px;border-radius:50%;border:3px solid var(--red);background:var(--black);display:flex;align-items:center;justify-content:center}
.video-caption{position:absolute;left:476px;top:462px;color:var(--white)}
.video-caption h4{font-family:"Saira",sans-serif;font-style:italic;font-weight:700;font-size:28px;letter-spacing:1px;border-left:4px solid var(--red);padding-left:14px;line-height:28px}
.video-caption p{font-family:"Saira",sans-serif;font-size:27px;margin-top:14px;padding-left:16px}

/* sale */
.sale-card{width:218px;height:310px;background:var(--white);border-radius:6px;display:flex;flex-direction:column;align-items:center;padding-top:34px}
.sale-card h4{font-family:"Montserrat",sans-serif;font-weight:700;font-size:18px;color:var(--red)}
.sale-card .pill{margin-top:14px}
.sale-card .photo{margin-top:28px;width:150px;height:140px;border-radius:6px}

/* newsletter */
.newsletter{position:absolute;top:4464px;left:0;width:1200px;height:264px;text-align:center}
.newsletter h2{margin-top:72px;font-family:"Montserrat",sans-serif;font-weight:700;font-size:25px}
.newsletter p{margin-top:18px;font-style:italic;font-size:14px;color:var(--muted)}
.signup{position:absolute;left:350px;top:162px;display:flex}
.signup .field{width:354px;height:48px;border:1.5px solid #bdbdbd;border-radius:24px;text-align:left;padding:15px 18px;font-style:italic;font-size:14px;color:var(--muted)}
.signup .btn{width:144px;height:48px;border-radius:24px;background:var(--red);color:var(--white);font-family:"Montserrat",sans-serif;font-weight:700;font-size:15px;display:flex;align-items:center;justify-content:center;margin-left:2px}

/* footer */
.footer{position:absolute;top:4728px;left:0;width:1200px;height:405px;background:var(--black);color:#cfcfcf}
.footer .brand{left:130px;top:42px}
.footer .about{position:absolute;left:130px;top:118px;width:400px;font-size:13px;line-height:20px}
.cards-pay{position:absolute;left:128px;top:238px;display:flex;gap:10px}
.cards-pay i{display:block;width:60px;height:34px;border-radius:4px;background:var(--white)}
.fcol{position:absolute;top:46px}
.fcol h5{font-family:"Montserrat",sans-serif;font-weight:700;font-size:15px;color:var(--red);margin-bottom:18px}
.fcol li{list-style:none;font-size:13px;line-height:26.5px}
.copy{position:absolute;left:0;right:0;top:338px;text-align:center;font-size:13px}
.social{position:absolute;left:954px;top:328px;width:36px;height:36px;border-radius:50%;background:var(--red)}
</style>
</head>
<body>

<div class="topbar">
  <div class="welcome">Welcome to Quorvantelle!</div>
  <div class="links"><span>Healthcare Providers</span><span>Funding</span><span>About Us</span><span>Contact Us</span></div>
</div>

<header class="header">
  <div class="brand"><span class="brand-dot"></span><span class="brand-name">Quorvantelle</span></div>
  <nav class="nav"><span>Wheelchairs</span><span>Parts</span><span>Accessories</span><span>Bargain Center</span><span>Online Invoice</span><span>Scooters</span></nav>
  <div class="nav-icons">
    <span style="background:var(--ink)"><svg width="14" height="14" viewBox="0 0 14 14"><circle cx="6" cy="6" r="4" fill="none" stroke="#fff" stroke-width="2"/><line x1="9" y1="9" x2="12.5" y2="12.5" stroke="#fff" stroke-width="2"/></svg></span>
    <span style="background:var(--red)"><svg width="14" height="14" viewBox="0 0 14 14"><circle cx="7" cy="4.5" r="3" fill="#fff"/><path d="M1.5 13c0-3.5 2.5-5 5.5-5s5.5 1.5 5.5 5z" fill="#fff"/></svg></span>
    <span style="background:var(--red)"><svg width="15" height="14" viewBox="0 0 15 14"><path d="M1 1h2l2 8h7l2-6H4" fill="none" stroke="#fff" stroke-width="1.8"/><circle cx="6" cy="12" r="1.3" fill="#fff"/><circle cx="11" cy="12" r="1.3" fill="#fff"/></svg></span>
  </div>
</header>

<section class="hero">
  <div class="hero-photo" role="img" aria-label="Photo of a man in a red jacket seated in a wheelchair on a mountain summit"></div>
  <svg class="hero-panel" width="1200" height="574" viewBox="0 0 1200 574">
    <defs><linearGradient id="heroRed" x1="0" y1="0" x2="0" y2="1"><stop offset="0" stop-color="#e3262a"/><stop offset=".7" stop-color="#d61d20"/><stop offset="1" stop-color="#9e1114"/></linearGradient></defs>
    <polygon points="710,0 762,0 668,330" fill="#0e0e0e"/>
    <polygon points="762,0 1200,0 1200,574 600,574" fill="url(#heroRed)"/>
  </svg>
  <h1 class="hero-title">MAKING<br>LIFE EASY</h1>
  <div class="hero-btn">SHOP NOW</div>
  <div class="hero-dots"><i></i><i></i><i></i></div>
</section>

<section class="band grey" style="top:706px;height:550px"></section>
<h2 class="heading" style="position:absolute;top:780px;left:0;width:1200px">LATEST <span>PRODUCTS</span></h2>
<div class="arrow" style="left:68px;top:986px"><svg width="20" height="20" viewBox="0 0 20 20"><path d="M13 3 6 10l7 7" fill="none" stroke="#222" stroke-width="2.5"/></svg></div>
<div class="arrow" style="left:1102px;top:986px"><svg width="20" height="20" viewBox="0 0 20 20"><path d="m7 3 7 7-7 7" fill="none" stroke="#222" stroke-width="2.5"/></svg></div>
<div class="cards" style="top:856px">
  <div class="card"><div class="photo" role="img" aria-label="Black rigid active wheelchair" style="background:radial-gradient(circle,#7a7a7a,#f3f3f3 70%)"></div><div class="name">Active Wheelchair the Veltrano Compact - 2.0</div><div class="price">$8,200</div><div class="pill">SHOP NOW</div></div>
  <div class="card"><div class="photo" role="img" aria-label="Black contoured wheelchair back rest" style="background:radial-gradient(circle,#2a2a2a 30%,#f3f3f3 70%)"></div><div class="name">Ostrava® Contoura® Elite Deep Back</div><div class="price">$935</div><div class="pill">SHOP NOW</div></div>
  <div class="card"><div class="photo" role="img" aria-label="Junior folding wheelchair with red and blue accents" style="background:radial-gradient(circle,#8c9099,#f3f3f3 70%)"></div><div class="name">Ostrava<br>Stride3 Junior</div><div class="price">$2,750</div><div class="pill">SHOP NOW</div></div>
  <div class="card"><div class="photo" role="img" aria-label="Red electric wheelchair power attachment" style="background:radial-gradient(circle,#c43030,#f3f3f3 70%)"></div><div class="name">Glowline by Brenna Mobility 2.5</div><div class="price">$6,250</div><div class="pill">SHOP NOW</div></div>
</div>

<h2 class="heading" style="position:absolute;top:1340px;left:0;width:1200px">SHOP BY <span>CATEGORIES</span></h2>
<div class="view-all">View All</div>
<div class="cat big" style="left:128px;top:1424px;width:456px;height:458px"><div class="photo" role="img" aria-label="Close-up of a black active wheelchair" style="background:linear-gradient(180deg,#5a5d63 0%,#2e3035 50%,#e01b1b 82%)"></div><span class="label">ACTIVE WHEELCHAIRS</span></div>
<div class="cat" style="left:604px;top:1424px;width:226px;height:222px"><div class="photo" role="img" aria-label="Wheelchair wheel with coloured spokes" style="background:linear-gradient(180deg,#ffffff 0%,#e9e9ea 45%,#e01b1b 85%)"></div><span class="label">ACCESSORIES</span></div>
<div class="cat" style="left:846px;top:1424px;width:226px;height:222px"><div class="photo" role="img" aria-label="Black wheelchair back cushions" style="background:linear-gradient(180deg,#ffffff 0%,#cfcfcf 45%,#e01b1b 85%)"></div><span class="label">ACCESSORIES</span></div>
<div class="cat" style="left:604px;top:1662px;width:226px;height:220px"><div class="photo" role="img" aria-label="Pair of black wheelchair armrests" style="background:linear-gradient(180deg,#ffffff 0%,#d4d4d4 45%,#e01b1b 85%)"></div><span class="label">ARMRESTS</span></div>
<div class="cat" style="left:846px;top:1662px;width:226px;height:220px"><div class="photo" role="img" aria-label="Grey backpack for wheelchairs" style="background:linear-gradient(180deg,#ffffff 0%,#c9cacb 45%,#e01b1b 85%)"></div><span class="label">BAGS</span></div>

<section class="band grey" style="top:1980px;height:554px"></section>
<h2 class="heading" style="position:absolute;top:2058px;left:0;width:1200px">BEST SELLING <span>PRODUCTS</span></h2>
<div class="arrow" style="left:68px;top:2264px"><svg width="20" height="20" viewBox="0 0 20 20"><path d="M13 3 6 10l7 7" fill="none" stroke="#222" stroke-width="2.5"/></svg></div>
<div class="arrow" style="left:1102px;top:2264px"><svg width="20" height="20" viewBox="0 0 20 20"><path d="m7 3 7 7-7 7" fill="none" stroke="#222" stroke-width="2.5"/></svg></div>
<div class="cards" style="top:2134px">
  <div class="card"><div class="photo" role="img" aria-label="Red and black handcycle wheelchair" style="background:radial-gradient(circle,#b83a3a,#f3f3f3 70%)"></div><div class="name">Summit Lil Accelor - Handcycle Wheelchair</div><div class="price">$8,200</div><div class="pill">SHOP NOW</div></div>
  <div class="card"><div class="photo" role="img" aria-label="Pair of grey wheelchair brake locks" style="background:radial-gradient(circle,#6d757c,#f3f3f3 70%)"></div><div class="name">Hawkstop Brakes - Wheelchair Locks</div><div class="price">$935</div><div class="pill">SHOP NOW</div></div>
  <div class="card"><div class="photo" role="img" aria-label="Pair of black wheelchair gloves" style="background:radial-gradient(circle,#2f2f2f 25%,#f3f3f3 70%)"></div><div class="name">Movenza 4 Seasons Ultra-Grip Gloves</div><div class="price">$2,750</div><div class="pill">SHOP NOW</div></div>
  <div class="card"><div class="photo" role="img" aria-label="Black and green electric wheelchair attachment" style="background:radial-gradient(circle,#4f6a55,#f3f3f3 70%)"></div><div class="name">Vector 800 by KT9</div><div class="price">$6,250</div><div class="pill">SHOP NOW</div></div>
</div>

<h2 class="heading" style="position:absolute;top:2594px;left:0;width:1200px">HAPPY <span>CUSTOMERS</span></h2>
<div class="customer" style="left:0;width:260px;background:linear-gradient(135deg,#d5d8dc,#5c6066 60%,#1f2023)" role="img" aria-label="Wheelchair fitted with an electric drive attachment"></div>
<div class="customer" style="left:280px;width:642px;background:linear-gradient(180deg,#2d3a2c 0%,#1d2421 55%,#101214 100%)" role="img" aria-label="Customer playing wheelchair basketball on an outdoor court">
  <div class="quote"><h3>DAREN HOLT</h3><p>Lorem ipsum dolor sit amet, consectetur adipiscing elit, sed do eiusmod tempor incididunt ut labore et dolore magna aliqum suspen.</p></div>
</div>
<div class="customer" style="left:940px;width:260px;background:linear-gradient(180deg,#b9c7cf 0%,#8aa1a8 45%,#52626a 100%)" role="img" aria-label="Smiling young girl seated in a light blue wheelchair outdoors"></div>

<h2 class="heading" style="position:absolute;top:3240px;left:0;width:1200px">WATCH OUR <span>TECHNOLOGY VIDEO</span></h2>
<section class="video" role="img" aria-label="Video still of a black wheelchair frame in close-up">
  <div class="play"><svg width="24" height="28" viewBox="0 0 24 28"><path d="M3 2v24l19-12z" fill="#fff"/></svg></div>
  <div class="video-caption"><h4>FLUXFORM TECHNOLOGY</h4><p>Striking lines, better performance.</p></div>
</section>

<section class="band grey" style="top:3910px;height:554px"></section>
<h2 class="heading" style="position:absolute;top:3988px;left:0;width:1200px">WHEELCHAIRS <span>FOR SALE</span></h2>
<div class="arrow" style="left:68px;top:4200px"><svg width="20" height="20" viewBox="0 0 20 20"><path d="M13 3 6 10l7 7" fill="none" stroke="#222" stroke-width="2.5"/></svg></div>
<div class="arrow" style="left:1102px;top:4200px"><svg width="20" height="20" viewBox="0 0 20 20"><path d="m7 3 7 7-7 7" fill="none" stroke="#222" stroke-width="2.5"/></svg></div>
<div class="cards" style="top:4066px">
  <div class="sale-card"><h4>ACTIVE</h4><div class="pill">SHOP NOW</div><div class="photo" role="img" aria-label="White active wheelchair" style="background:radial-gradient(circle,#9a9a9a,#f5f5f5 70%)"></div></div>
  <div class="sale-card"><h4>STANDARD</h4><div class="pill">SHOP NOW</div><div class="photo" role="img" aria-label="Black standard folding wheelchair" style="background:radial-gradient(circle,#555,#f5f5f5 70%)"></div></div>
  <div class="sale-card"><h4>SPORT</h4><div class="pill">SHOP NOW</div><div class="photo" role="img" aria-label="Blue sport wheelchair with cambered wheels" style="background:radial-gradient(circle,#3a4f8c,#f5f5f5 70%)"></div></div>
  <div class="sale-card"><h4>PAEDIATRIC</h4><div class="pill">SHOP NOW</div><div class="photo" role="img" aria-label="Yellow and black paediatric wheelchair" style="background:radial-gradient(circle,#c9b42a,#f5f5f5 70%)"></div></div>
</div>

<section class="newsletter">
  <h2>SIGN UP FOR NEWSLETTER</h2>
  <p>Lorem ipsum dolor sit amet, consectetur adipiscing elit, sed do eiusmod</p>
  <div class="signup"><div class="field">Email Address</div><div class="btn">SIGNUP</div></div>
</section>

<footer class="footer">
  <div class="brand"><span class="brand-dot"></span><span class="brand-name">Quorvantelle</span></div>
  <p class="about">At Quorvantelle we are all about Making Life Easier. Quorvantelle is an online business focusing on providing choice and an easier shopping experience to those people that need the use of a wheelchair.</p>
  <div class="cards-pay" aria-label="Accepted payment methods"><i></i><i></i><i></i><i></i></div>
  <div class="fcol" style="left:618px"><h5>QUICK LINKS</h5><ul><li>Search</li><li>About us</li><li>Privacy Policy</li><li>Postage</li><li>International Shipping</li><li>Terms of Service</li><li>Returns Policy</li></ul></div>
  <div class="fcol" style="left:882px"><h5>NAV</h5><ul><li>Wheelchairs</li><li>Parts</li><li>Accessories</li><li>Bargain Center</li><li>Online Invoice/Quotes</li><li>Scooters</li></ul></div>
  <div class="copy">© 2023 Quorvantelle.. All rights are Reserved.</div>
  <div class="social" aria-label="Social media"></div>
</footer>

</body>
</html>
```